依頼詳細
商品名は「WHEY PROTEIN ISOLATE」です。一般的なプロテインよりも脂肪・糖質を極力排除しており、高純度のたんぱく質を摂取でき、効率的に引き締まった体を作れるのが特徴になります。

メインユーザーは30~40代。男女比はほぼ1:1です。

現行のものは栄養士またはトレーナーがカウンセリングしてから提供することを想定して、名前・量・飲み方を記載して提供できるようにしています(添付ファイルをご覧下さいませ)。レイアウトやデザインは変えてもいいですが、これらの項目自体は変えないようにお願いいたします。

現行品のシンプルさ・清潔感を保ちつつも、「プレミアム」な印象を持てるものになると嬉しいです。

<例1(フォルテン)>
http://shop.forten.jp/products/list.php?category_id=7
<例2(ネクサリオン)>
https://www.nexarion.jp/sports-nutrition/solid-core-blend/48271605.html

以上、よいご提案をお待ちしております。
ご不明な点がございましたら、お気軽にお問い合せ下さいませ。
記載項目
スタンドアルミパウチ:横218mm×縦340mm(チャック下310mm)
※現行品はシールに印刷して貼っていますが、リニューアル品はパウチに印刷しますので、印刷範囲の指定はございません。
希望イメージ
シンプル 複雑
単色 カラフル
暗い 明るい
日常 高級
遊び心 厳粛
未来的 伝統的
女性的 男性的
希望する色
カラーは白地にエメラルドグリーン(DIC63)でお願いいたします。他の色を追加してもOKです。
納品ファイル
• イラストレーター形式 (.ai)
補足説明
選定後はアウトライン化されているファイルと、されていないファイルの両方をお送り下さい。
パーソナルジムに陳列するプロテインですので…あまりにエステっぽいといいますか、女性的なデザインは好ましくないかと思います。
重ねて申し上げますが、シンプルにお願いいたします。<例>もよくご覧下さいませ。
■ 選んだ理由

他にもいいご提案があり悩みましたが、インストラクション部分のデザインが見やすい点が決め手になりました。

■ 提案者全員のお礼・コメント

たくさんのご提案ありがとうございました。また機会がありましたらぜひよろしくお願い致します。

```html
<!DOCTYPE html>
<html lang="en">
<head>
<meta charset="utf-8">
<title>Whey Protein Isolate – Pouch Front</title>
<link rel="stylesheet" href="https://fonts.googleapis.com/css2?family=Archivo+Black&family=Roboto:wght@400;700&display=swap">
<style>
  :root {
    --pouch-white: #ffffff;
    --page-bg: #f1f1f1;
    --gold-dark: #9c7d2c;
    --gold-mid: #c6a553;
    --gold-light: #e2cd86;
    --gold-edge: #7d6221;
    --tagline-ink: #3b2f10;
    --ink: #3a3a3a;
    --ink-soft: #6b6b6b;
    --rule: #9a9a9a;
    --emerald: #1f9e5a;
  }
  html, body {
    margin: 0;
    width: 763px;
    height: 1200px;
    overflow: hidden;
    background: var(--page-bg);
  }
  .pouch {
    position: relative;
    width: 763px;
    height: 1200px;
    background: linear-gradient(90deg, #f4f4f4 0%, var(--pouch-white) 12%, var(--pouch-white) 88%, #f2f2f2 100%);
    font-family: "Roboto", sans-serif;
    color: var(--ink);
  }
  .zipper-zone {
    position: absolute;
    left: 0; right: 0; top: 40px;
    height: 90px;
  }
  .zipper-line {
    position: absolute;
    left: 0; right: 0; top: 58px;
    border-top: 2px dashed #c9c9c9;
  }
  .zipper-note {
    position: absolute;
    left: 110px; top: 20px;
    font-size: 13px;
    color: var(--ink-soft);
    letter-spacing: 1px;
  }
  .zipper-note.secondary { left: 300px; top: 70px; font-size: 11px; }
  .seal-box {
    position: absolute;
    right: 90px; top: 62px;
    width: 60px; height: 16px;
    border: 1px solid var(--rule);
  }
  .recycle-mark {
    position: absolute;
    right: 36px; top: 40px;
    width: 34px; height: 34px;
    border: 2px solid var(--ink-soft);
  }
  .label-panel {
    position: absolute;
    left: 34px; right: 34px; top: 230px;
    height: 400px;
    box-sizing: border-box;
    padding: 30px 40px 0;
    background: linear-gradient(135deg, var(--gold-dark) 0%, var(--gold-mid) 40%, var(--gold-light) 60%, var(--gold-mid) 80%, var(--gold-dark) 100%);
    box-shadow: inset 0 0 0 3px var(--gold-edge);
    text-align: center;
    color: #fff;
  }
  .label-panel::before {
    content: "";
    position: absolute;
    inset: 14px;
    border: 2px solid rgba(255,255,255,0.55);
    pointer-events: none;
  }
  .brand-dot {
    display: block;
    width: 28px; height: 28px;
    margin: 0 auto;
    border-radius: 50%;
    background: var(--emerald);
  }
  .product-name {
    margin: 6px 0 0;
    font-family: "Archivo Black", sans-serif;
    font-weight: 400;
    line-height: 0.98;
  }
  .product-name .line-main {
    display: block;
    font-size: 90px;
    letter-spacing: 1px;
  }
  .product-name .line-sub {
    display: block;
    font-size: 40px;
    margin-top: 4px;
    letter-spacing: 3px;
  }
  .tagline {
    margin: 14px auto 0;
    width: 440px;
    font-size: 12px;
    line-height: 1.4;
    font-weight: 700;
    color: var(--tagline-ink);
  }
  .instruction-form {
    position: absolute;
    left: 70px; right: 70px; top: 665px;
    display: grid;
    grid-template-columns: 1fr 1fr;
    column-gap: 56px;
    font-size: 15px;
  }
  .field-title {
    font-weight: 700;
    font-size: 14px;
    margin: 0 0 6px;
  }
  .write-line {
    height: 26px;
    border-bottom: 1px solid var(--rule);
    margin-bottom: 24px;
  }
  .option-list {
    list-style: none;
    margin: 0; padding: 0;
  }
  .option-list li {
    display: flex;
    align-items: center;
    gap: 12px;
    height: 36px;
    border-bottom: 1px solid var(--rule);
    padding-left: 22px;
  }
  .checkbox {
    width: 13px; height: 13px;
    border: 1.5px solid var(--ink);
    flex: none;
  }
  .inline-options {
    display: flex;
    align-items: center;
    gap: 12px;
    height: 26px;
    padding-left: 22px;
    border-bottom: 1px solid var(--rule);
    margin-bottom: 24px;
  }
  .brand-sign {
    position: absolute;
    left: 0; right: 0; top: 1010px;
    display: flex;
    justify-content: center;
    align-items: center;
    gap: 10px;
    font-family: "Archivo Black", sans-serif;
    font-size: 28px;
    letter-spacing: 4px;
    color: var(--emerald);
  }
  .brand-sign .mark {
    width: 22px; height: 22px;
    border-radius: 50%;
    background: var(--emerald);
  }
</style>
</head>
<body>
<main class="pouch">
  <div class="zipper-zone">
    <span class="zipper-note">OPEN HERE</span>
    <span class="zipper-note secondary">Close zipper firmly after each use</span>
    <div class="zipper-line"></div>
    <div class="seal-box"></div>
    <div class="recycle-mark"></div>
  </div>

  <section class="label-panel">
    <span class="brand-dot"></span>
    <h1 class="product-name">
      <span class="line-main">WHEY</span>
      <span class="line-main">PROTEIN</span>
      <span class="line-sub">ISOLATE</span>
    </h1>
    <p class="tagline">The future you is built from what you eat now.<br>The only way to realize your dream<br>is to keep taking one small step at a time.</p>
  </section>

  <section class="instruction-form">
    <div class="form-column">
      <p class="field-title">Name</p>
      <div class="write-line"></div>
      <p class="field-title">Recommended intake per once</p>
      <ul class="option-list">
        <li><span class="checkbox"></span>2 SPOON / 200cc</li>
        <li><span class="checkbox"></span>3 SPOON / 300cc</li>
        <li><span class="checkbox"></span>4 SPOON / 400cc</li>
        <li><span class="checkbox"></span>(&emsp;&emsp;&emsp;&emsp;&emsp;&emsp;)</li>
      </ul>
    </div>
    <div class="form-column">
      <p class="field-title">Drink</p>
      <div class="inline-options"><span class="checkbox"></span>WATER /<span class="checkbox"></span>MILK</div>
      <p class="field-title">Recommended timing</p>
      <ul class="option-list">
        <li><span class="checkbox"></span>BREAKFAST</li>
        <li><span class="checkbox"></span>AFTER EXERCIZE</li>
        <li><span class="checkbox"></span>BEFORE SLEEP</li>
        <li><span class="checkbox"></span>(&emsp;&emsp;&emsp;&emsp;&emsp;&emsp;)</li>
      </ul>
    </div>
  </section>

  <div class="brand-sign"><span class="mark"></span>VERDANT</div>
</main>
</body>
</html>
```